Need DL Flyer for Real Estate Drops

We need a real estate flyer ,double sided. With content on 1 side like: Want to know what's your house is worth " contact us today and on other side agent details. We are looking for an ongoing partnership with designer so this assignment will be ongoing

```html
<!DOCTYPE html>
<html lang="en">
<head>
<meta charset="utf-8">
<title>Mirage Real Estate – DL Flyer</title>
<link href="https://fonts.googleapis.com/css2?family=Montserrat:wght@400;500;700;800;900&display=swap" rel="stylesheet">
<style>
  :root{
    --bg:#e4e4e6;
    --paper:#ffffff;
    --red:#d3222a;
    --ink:#1c1c24;
    --navy:#1f2033;
    --grey:#b9bdc3;
    --line:#e9b9a0;
  }
  *{box-sizing:border-box;margin:0;padding:0}
  html,body{width:1200px;height:857px;overflow:hidden;background:var(--bg);font-family:'Montserrat',sans-serif;color:var(--ink)}
  .stage{position:relative;width:1200px;height:857px}
  .flyer{position:absolute;top:48px;width:360px;height:760px;background:var(--paper);box-shadow:0 8px 24px rgba(0,0,0,.12);overflow:hidden}
  .flyer--partnership{left:210px;display:flex;flex-direction:column;align-items:center}
  .flyer--valuation{left:630px}
  .flyer__art{display:block;width:360px;flex:none}
  .flyer--valuation .flyer__art{position:absolute;left:0;top:0}

  .brand{display:flex;align-items:center;gap:10px}
  .brand__mark{width:34px;height:34px;background:var(--red)}
  .brand__name{font-weight:700;font-size:40px;line-height:1;color:var(--navy);letter-spacing:.5px}
  .brand__sub{font-weight:500;font-size:10px;letter-spacing:4px;color:var(--navy);text-align:right;margin-top:2px}
  .flyer--partnership .brand{align-self:flex-start;margin-left:40px;margin-top:4px}

  .section-title{margin-top:14px;text-align:center;font-weight:800;font-size:15px;letter-spacing:1px}
  .body-copy{margin-top:6px;padding:0 30px;text-align:center;font-size:10.5px;line-height:1.4}
  .body-copy p+p{margin-top:6px}

  .swoosh{display:block;width:240px;height:20px}
  .flyer--partnership .swoosh{margin-top:10px;flex:none}
  .contact{text-align:center}
  .flyer--partnership .contact{margin-top:2px}
  .contact__cta{font-weight:800;font-size:17px;letter-spacing:.5px;line-height:1.25}
  .contact__addr{font-weight:700;font-size:11px;line-height:1.3}
  .contact__phone{font-weight:800;font-size:24px;line-height:1.15}
  .contact__web{font-weight:700;font-size:14px;line-height:1.3}

  .tab{position:absolute;right:20px;top:0;width:170px;height:118px;background:var(--red);color:#fff;display:flex;flex-direction:column;align-items:center;justify-content:center}
  .tab .brand__name{color:#fff;font-size:34px}
  .tab .brand__sub{color:#fff;text-align:center;font-size:9px}
  .tab__dot{width:14px;height:14px;background:#fff;margin-bottom:8px}
  .headline{position:absolute;left:0;right:0;top:500px;text-align:center;color:var(--red);font-weight:900;line-height:1}
  .headline__lead{font-size:19px;letter-spacing:.5px}
  .headline__main{font-size:58px;letter-spacing:1px}
  .flyer--valuation .swoosh{position:absolute;left:60px;top:588px}
  .flyer--valuation .contact{position:absolute;left:0;right:0;top:614px}
</style>
</head>
<body>
<main class="stage">

  <article class="flyer flyer--partnership">
    <svg class="flyer__art" viewBox="0 0 360 392" height="392">
      <defs>
        <linearGradient id="kitchen" x1="0" y1="0" x2="1" y2="1"><stop offset="0" stop-color="#4a3a33"/><stop offset="1" stop-color="#d8d8d6"/></linearGradient>
        <linearGradient id="dining" x1="0" y1="0" x2="0" y2="1"><stop offset="0" stop-color="#3b2d27"/><stop offset="1" stop-color="#8a8e96"/></linearGradient>
        <linearGradient id="exterior" x1="0" y1="0" x2="0" y2="1"><stop offset="0" stop-color="#c9825e"/><stop offset=".45" stop-color="#9aa0a4"/><stop offset="1" stop-color="#6b6e70"/></linearGradient>
        <linearGradient id="galley" x1="0" y1="0" x2="0" y2="1"><stop offset="0" stop-color="#4a3a33"/><stop offset="1" stop-color="#e3e3e3"/></linearGradient>
      </defs>
      <polyline points="30,200 170,135 320,240" fill="none" stroke="var(--line)" stroke-width="1"/>
      <polygon role="img" aria-label="Photo of a modern kitchen with dark timber ceiling" fill="url(#kitchen)" points="15,12 92,12 130,78 92,144 15,144 -23,78"/>
      <polygon role="img" aria-label="Photo of an open dining area with blue chairs" fill="url(#dining)" points="165,80 242,80 280,146 242,212 165,212 127,146"/>
      <polygon role="img" aria-label="Photo of a grey rendered home exterior at sunset" fill="url(#exterior)" points="35,155 112,155 150,221 112,287 35,287 -3,221"/>
      <polygon role="img" aria-label="Photo of a white galley kitchen" fill="url(#galley)" points="175,228 252,228 290,294 252,360 175,360 137,294"/>
      <polyline points="315,70 325,82 315,94 325,106" fill="none" stroke="var(--grey)" stroke-width="2"/>
      <polyline points="324,70 334,82 324,94 334,106" fill="none" stroke="var(--grey)" stroke-width="2"/>
      <circle cx="300" cy="378" r="5" fill="none" stroke="var(--grey)"/>
      <circle cx="24" cy="315" r="4" fill="none" stroke="var(--grey)"/>
    </svg>

    <div class="brand">
      <span class="brand__mark"></span>
      <div>
        <div class="brand__name">mirage</div>
        <div class="brand__sub">REAL ESTATE</div>
      </div>
    </div>

    <h2 class="section-title">PARTNERSHIP</h2>
    <div class="body-copy">
      <p>Lorem ipsum dolor sit amet, consectetuer adipiscing elit, sed diam nonummy nibh euismod tincidunt ut laoreet dolore magna aliquam erat volutpat. Ut wisi enim ad minim veniam, quis nostrud exerci tation ullamcorper suscipit lobortis nisl ut aliquip.</p>
      <p>Lorem ipsum dolor sit amet, consectetuer aliquam erat volutpat. Ut wisi enim ad minim veniam, quis nostrud exerci tation.</p>
    </div>

    <svg class="swoosh" viewBox="0 0 240 22" aria-hidden="true"><path d="M4 4 Q120 30 236 16 Q120 22 4 4Z" fill="var(--ink)"/></svg>
    <div class="contact">
      <div class="contact__cta">CONTACT US TODAY</div>
      <div class="contact__addr">14/8 Horizon Ave, Westfield, VIC 3040</div>
      <div class="contact__phone">(03) 9012 3456</div>
      <div class="contact__web">www.miragerealestate.com.au</div>
    </div>
  </article>

  <article class="flyer flyer--valuation">
    <svg class="flyer__art" viewBox="0 0 360 480" height="480">
      <defs>
        <linearGradient id="facade" x1="0" y1="0" x2="0" y2="1"><stop offset="0" stop-color="#c9825e"/><stop offset=".5" stop-color="#8c9094"/><stop offset="1" stop-color="#4f8f3a"/></linearGradient>
        <linearGradient id="bath" x1="0" y1="0" x2="0" y2="1"><stop offset="0" stop-color="#e2e2e2"/><stop offset="1" stop-color="#3a3a3e"/></linearGradient>
        <linearGradient id="bedroom" x1="0" y1="0" x2="0" y2="1"><stop offset="0" stop-color="#d9d9dc"/><stop offset="1" stop-color="#a8c4c6"/></linearGradient>
        <linearGradient id="lounge" x1="0" y1="0" x2="0" y2="1"><stop offset="0" stop-color="#d6d4d0"/><stop offset="1" stop-color="#55585e"/></linearGradient>
      </defs>
      <polyline points="20,330 180,250 340,300" fill="none" stroke="var(--line)" stroke-width="1"/>
      <polygon role="img" aria-label="Photo of a grey home facade with lawn" fill="url(#facade)" points="50,130 130,130 170,199 130,268 50,268 10,199"/>
      <polygon role="img" aria-label="Photo of a bathroom vanity with round mirror" fill="url(#bath)" points="180,180 260,180 300,249 260,318 180,318 140,249"/>
      <polygon role="img" aria-label="Photo of a bedroom with artwork above the bed" fill="url(#bedroom)" points="50,285 130,285 170,354 130,423 50,423 10,354"/>
      <polygon role="img" aria-label="Photo of a living room with sofa" fill="url(#lounge)" points="180,335 260,335 300,404 260,473 180,473 140,404"/>
      <polyline points="318,150 328,162 318,174 328,186" fill="none" stroke="var(--grey)" stroke-width="2"/>
      <polyline points="327,150 337,162 327,174 337,186" fill="none" stroke="var(--grey)" stroke-width="2"/>
      <circle cx="20" cy="440" r="5" fill="none" stroke="var(--grey)"/>
      <circle cx="320" cy="470" r="5" fill="none" stroke="var(--grey)"/>
    </svg>

    <div class="tab">
      <span class="tab__dot"></span>
      <div class="brand__name">mirage</div>
      <div class="brand__sub">REAL ESTATE</div>
    </div>

    <h1 class="headline">
      <div class="headline__lead">WHAT'S YOUR HOUSE IS</div>
      <div class="headline__main">WORTH?</div>
    </h1>

    <svg class="swoosh" viewBox="0 0 240 22" aria-hidden="true"><path d="M4 4 Q120 30 236 16 Q120 22 4 4Z" fill="var(--ink)"/></svg>
    <div class="contact">
      <div class="contact__cta">CONTACT US TODAY</div>
      <div class="contact__addr">14/8 Horizon Ave, Westfield, VIC 3040</div>
      <div class="contact__phone">(03) 9012 3456</div>
      <div class="contact__web">www.miragerealestate.com.au</div>
    </div>
  </article>

</main>
</body>
</html>
```